WANTED: The Best Mobile App Designers

We are looking for the best mobile app designers.

This is a small test job to test your skills and the winner will be given ongoing work which means ongoing work and revenue for you!

If you do not feel you are the BEST please DO NOT APPLY as we are only looking for "the" best mobile app designers with experience.

Attached is a test spec for a design we need.

Look forward to seeing your skills and creating a long term relationship.

Target Market(s)

General consumers who are looking to sell their unwanted items to make extra cash

Industry/Entity Type

Work

Requirements
Must have
• The designs must match and look great with the attached logo.

Design must be top quality and give the impression of a billion dollar company.

```html
<!DOCTYPE html>
<html lang="en">
<head>
<meta charset="utf-8">
<title>SwapNest – Listing Description</title>
<link rel="stylesheet" href="https://fonts.googleapis.com/css2?family=Roboto:ital,wght@0,400;0,500;1,300&family=Arimo:wght@400&display=swap">
<style>
  :root {
    --page-bg: #e9eaec;
    --frame: #1d1d1d;
    --screen-bg: #ececec;
    --header-top: #6b6b6b;
    --header-bottom: #3f3f3f;
    --tagline: #e8e8e8;
    --brand-dot: #19a4e2;
    --card-bg: #ffffff;
    --card-border: #cfcfcf;
    --heading: #2f2f2f;
    --body-text: #4a4a4a;
    --band-top: #555555;
    --band-bottom: #333333;
    --photo-warm: #f29a2e;
    --photo-dark: #3b2414;
    --button-top: #ffb815;
    --button-bottom: #f59b00;
    --button-text: #3a2a12;
    --muted: #7a7a7a;
    --star: #f6a417;
    --icon-grey: #6f6f6f;
    --bubble-border: #bdbdbd;
  }
  * { box-sizing: border-box; margin: 0; padding: 0; }
  html, body { width: 1200px; height: 2260px; overflow: hidden; background: var(--page-bg); }
  .screen {
    position: absolute; left: 55px; top: 320px; width: 1090px; height: 1620px;
    background: var(--screen-bg); border: 11px solid var(--frame); border-radius: 10px; overflow: hidden;
    font-family: "Roboto", Arial, sans-serif;
  }
  .app-header {
    position: absolute; left: 0; top: 0; width: 100%; height: 150px;
    background: linear-gradient(180deg, var(--header-top), var(--header-bottom));
    display: flex; align-items: center; justify-content: center; gap: 22px;
  }
  .brand { display: flex; align-items: center; gap: 14px; }
  .brand-dot { width: 74px; height: 74px; border-radius: 50%; background: var(--brand-dot); }
  .brand-name { font-weight: 500; font-size: 44px; color: #ffffff; }
  .tagline { font-style: italic; font-weight: 300; font-size: 42px; color: var(--tagline); }

  .listing-card {
    position: absolute; left: 46px; top: 181px; width: 999px; height: 913px;
    background: var(--card-bg); border: 2px solid var(--card-border);
  }
  .section-title { position: absolute; left: 41px; top: 22px; font-size: 60px; font-weight: 500; color: var(--heading); }
  .description { position: absolute; left: 22px; top: 114px; width: 953px; }
  .product-photo {
    float: left; width: 432px; height: 338px; margin: 0 24px 8px 0;
    background: radial-gradient(ellipse at 70% 20%, var(--photo-warm), #a65a1c 45%, var(--photo-dark) 90%);
  }
  .product-name { font-size: 60px; font-weight: 400; color: #444; line-height: 74px; margin-top: 10px; }
  .body-copy {
    font-family: "Arimo", Arial, sans-serif; font-size: 24.5px; line-height: 28.5px;
    color: var(--body-text); text-align: justify;
  }
  .offer-band {
    position: absolute; left: 0; top: 633px; width: 100%; height: 72px;
    background: linear-gradient(110deg, var(--band-bottom) 0%, var(--band-top) 85%, #6a6a6a 86%, var(--band-top) 100%);
    color: #fff; font-size: 36px; font-weight: 500; padding: 14px 30px;
  }
  .offer-copy { position: absolute; left: 22px; top: 722px; width: 953px; }

  .ask-button {
    position: absolute; left: 157px; top: 1129px; width: 775px; height: 122px;
    background: linear-gradient(180deg, var(--button-top), var(--button-bottom));
    border-radius: 6px; display: flex; align-items: center; justify-content: center;
    font-size: 47px; font-weight: 500; color: var(--button-text);
  }
  .rep-title { position: absolute; left: 59px; top: 1305px; font-size: 47px; color: var(--heading); text-decoration: underline; text-underline-offset: 8px; }
  .rep-label { position: absolute; font-size: 38px; color: var(--muted); }
  .stars { position: absolute; left: 305px; top: 1386px; }
  .feedback-bubble {
    position: absolute; left: 265px; top: 1462px; width: 454px; height: 78px;
    border: 2px solid var(--bubble-border); border-radius: 6px; background: #fff;
    font-family: "Arimo", Arial, sans-serif; font-size: 19px; line-height: 24px; color: #444; padding: 9px 14px;
  }
  .feedback-bubble::after {
    content: ""; position: absolute; left: 30px; bottom: -16px; width: 24px; height: 24px;
    background: #fff; border-right: 2px solid var(--bubble-border); border-bottom: 2px solid var(--bubble-border);
    transform: skewY(45deg) rotate(0deg); clip-path: polygon(0 0,100% 0,100% 100%);
  }
  .verify-icon { position: absolute; top: 1463px; width: 72px; height: 72px; border-radius: 50%; background: var(--icon-grey); }
</style>
</head>
<body>
  <main class="screen">
    <header class="app-header">
      <div class="brand"><span class="brand-dot"></span><span class="brand-name">SwapNest</span></div>
      <span class="tagline">Sell, Buy, Rent Anything!</span>
    </header>

    <section class="listing-card">
      <h1 class="section-title">Description:</h1>
      <div class="description">
        <div class="product-photo" role="img" aria-label="Product photo of a smartphone lying on a wooden table under warm light"></div>
        <h2 class="product-name">Lumo 5</h2>
        <p class="body-copy">Sed ut perspiciatis unde omnis iste natus error sit voluptatem accusantium doloremque laudantium, totam rem aperiam, eaque ipsa quae ab illo inventore veritatis et quasi architecto beatae vitae dicta sunt explicabo. Nemo enim ipsam voluptatem quia voluptas sit aspernatur aut odit aut fugit,sedquia consequuntur magni dolores qui in ea voluptate velit esse quam nihil molestiae consequatur, vel illum qui dolorem eum fugiat quo voluptas nulla pariatur.qui in ea voluptate velit esse qu am nihil molestiae consequatur, vel illum qui dolorem eum fugiat quo voluptas nulla pariatur.</p>
      </div>
      <div class="offer-band">User Offer By Type:</div>
      <p class="body-copy offer-copy">qui in ea voluptate velit esse quam nihil molestiae consequatur, vel illum qui dolorem eum fugiat quo voluptas nulla pariatur.qui in ea voluptate velit esse qu am nihil molestiae consequatur, vel illum qui dolorem eum fugiat quo voluptas nulla pariatur.</p>
    </section>

    <div class="ask-button">ASK ME A QUESTION?</div>

    <h3 class="rep-title">Sellers Rep:</h3>
    <span class="rep-label" style="left:59px; top:1386px;">Stars Rating</span>
    <svg class="stars" width="230" height="50" viewBox="0 0 230 50" aria-label="4.5 out of 5 stars">
      <defs>
        <polygon id="star" points="23,2 29,17 45,18 33,28 37,44 23,35 9,44 13,28 1,18 17,17"/>
        <clipPath id="half-star"><rect x="0" y="0" width="23" height="50"/></clipPath>
      </defs>
      <use href="#star" x="0" fill="#f6a417"/>
      <use href="#star" x="45" fill="#f6a417"/>
      <use href="#star" x="90" fill="#f6a417"/>
      <use href="#star" x="135" fill="#f6a417"/>
      <use href="#star" x="180" fill="none" stroke="#f6a417" stroke-width="2.5"/>
      <g clip-path="url(#half-star)" transform="translate(180,0)"><use href="#star" fill="#f6a417"/></g>
    </svg>
    <span class="rep-label" style="left:751px; top:1386px;">Verification</span>

    <span class="rep-label" style="left:59px; top:1475px;">Feedback</span>
    <div class="feedback-bubble">Sed ut perspiciatis unde omnis iste natus error sit voluptatem accusantium dolor</div>

    <span class="verify-icon" style="left:753px;"></span>
    <span class="verify-icon" style="left:834px;"></span>
    <span class="verify-icon" style="left:915px;"></span>
  </main>
</body>
</html>
```